Modify mobile web Photoshop design to make them look great

We need to choose and refine the stock image to look great on 5 mobile web pages: 1) Hourglass image on home screen, 2) Sofa image on registration screen, 3) Loveseat image on login screen, 4) Lamp for reminder screen, and 5) Bed for ratings / score screen. Sample photos denote what customer wants, but they are just downloaded from Brindo, and is not purchased stock photos. Designers need to show that the updated photos used are properly purchased from stock photo source. Photoshop files for all 5 mobile web pages are provided. Artists are requested to edit and submit the 5 photoshop files and make them look as good as possible with the constraints above. No change is needed on the layout or anything beside the 5 stock images, but subtle refinements are OK if you believe it would improve the overall design without affecting the art direction.

Target Market(s)

Travel, Lifestyle

Industry/Entity Type

Hospitality

Font styles to use
Sans Serif

Requirements
Must have
• Stock photos must be properly licensed, artists must put updated stock photos back into supplied photoshop source files, updated look and feel should have the same general art direction, images must be hourglass, sofa, loveseat, lamp and bed
Nice to have
• Minor and very subtle touchup of other elements without affecting any design work of the layout such as color scheme
Should not have
• Should not affect art direction, identity and color of all design and layout elements, should not use stock image other than the types specified (hourglass, sofa, loveseat, lamp and bed), should not use images not licensed from stock photo sites

```html
<!DOCTYPE html>
<html lang="en">
<head>
<meta charset="utf-8">
<title>Lodgia mobile screens</title>
<link href="https://fonts.googleapis.com/css2?family=Roboto:wght@400;500;700&family=Fjalla+One&display=swap" rel="stylesheet">
<style>
:root{
  --board:#808080;
  --magenta:#a0177f;
  --teal:#0f9a94;
  --lilac:#b27fd8;
  --orange:#d98a55;
  --peach:#e8b896;
  --peach-light:#f3d6bd;
  --soft:#fbf3ec;
  --grey:#b9b9b9;
  --ink:#1e1e1e;
  --white:#ffffff;
}
*{box-sizing:border-box;margin:0;padding:0}
html,body{width:1200px;height:1200px;overflow:hidden;background:var(--board);font-family:'Roboto',sans-serif;color:var(--ink)}
.board{position:relative;width:1200px;height:1200px}
.screen{position:absolute;background:var(--white);overflow:hidden}
.abs{position:absolute}
.header{position:absolute;left:0;top:0;width:100%;background:var(--white)}
.brand{position:absolute;left:0;width:100%;text-align:center;font-weight:700;font-size:27px;letter-spacing:-1px;color:var(--ink)}
.brand.color{color:var(--magenta)}
.menu{position:absolute;right:14px;width:19px;height:12px;border-top:1.6px solid #333;border-bottom:1.6px solid #333}
.menu::after{content:"";position:absolute;left:0;right:0;top:4px;border-top:1.6px solid #333}
.back{position:absolute;left:20px;width:11px;height:11px;border-left:2.6px solid #222;border-bottom:2.6px solid #222;transform:rotate(45deg)}
.photo{position:absolute;left:0;width:100%}
.dots{position:absolute;left:0;width:100%;display:flex;justify-content:center;gap:8px}
.dots i{width:10px;height:10px;border-radius:50%;display:block}
.d1{background:var(--lilac)}.d2{background:var(--teal)}.d3{background:var(--magenta)}.d4{background:#f0b27a}.dk{background:#111}

/* home */
.hero{top:40px;height:229px;background:radial-gradient(circle at 78% 40%,#f4e3cc 0,#c89a68 30%,#8a5a30 70%,#5e3a1c 100%)}
.home-body{position:absolute;left:0;top:269px;width:100%;height:278px;background:var(--orange)}
.home-card{position:absolute;left:20px;top:18px;width:328px;height:255px;background:var(--peach);border-radius:4px}
.title-hotel{position:absolute;left:0;width:100%;top:94px;text-align:center;font-family:'Fjalla One',sans-serif;font-size:46px;line-height:46px}
.title-sub{position:absolute;left:0;width:100%;top:140px;text-align:center;font-family:'Fjalla One',sans-serif;font-size:15px;letter-spacing:1px}
.search{position:absolute;left:8px;top:210px;width:312px;height:34px;display:flex;background:var(--grey);border-radius:4px;font-size:14px}
.search .s-main{flex:1;display:flex;align-items:center;justify-content:center;border-right:1px solid #ddd}
.search .s-region{width:68px;display:flex;align-items:center;justify-content:center;border-right:1px solid #ddd}
.search .s-go{width:38px;display:flex;align-items:center;justify-content:center}
.tiles{position:absolute;left:0;top:547px;width:100%;height:66px;display:flex}
.tile{flex:1;color:var(--white);font-size:9px;font-weight:700;display:flex;flex-direction:column;align-items:center;justify-content:center;gap:4px}
.t-leisure{background:var(--lilac)}.t-food{background:var(--teal)}.t-beauty{background:var(--magenta)}.t-life{background:#f4b98a}
.badge{position:absolute;top:620px;height:34px;background:#111;border-radius:4px}
.login-btn{position:absolute;right:10px;top:628px;width:76px;height:26px;background:#e4e4e4;border-radius:3px;font-size:11px;font-weight:700;display:flex;align-items:center;justify-content:center;gap:6px}

/* forms */
.band{position:absolute;left:0;width:100%;background:#e0b592}
.formbar{position:absolute;left:0;width:100%;height:32px;background:var(--magenta);color:var(--white);font-weight:700;font-size:13px;display:flex;align-items:center;justify-content:center}
.glass{position:absolute;background:rgba(245,232,222,.55);border:1px solid rgba(255,255,255,.7);border-radius:4px}
.field{position:absolute;height:27px;background:var(--white);border-bottom:1.5px solid var(--lilac);display:flex;align-items:center;font-size:10.5px;color:#333}
.field .ico{width:30px;height:100%;display:flex;align-items:center;justify-content:center;border-right:1px solid #ccc;margin-right:8px;font-size:8px;color:var(--magenta)}
.field.teal{border-bottom-color:var(--teal)}
.field.mag{border-bottom-color:var(--magenta)}
.btn{position:absolute;background:var(--magenta);color:var(--white);font-size:13px;display:flex;align-items:center;justify-content:center;border-radius:2px}

/* reminder */
.remind-card{position:absolute;left:12px;top:117px;width:344px;height:283px;background:rgba(243,234,226,.8);border-radius:4px;text-align:center}
.choice{position:absolute;height:22px;font-size:13px;display:flex;align-items:center;justify-content:center;border-radius:2px}

/* rating */
.rate-bg{position:absolute;left:0;top:45px;width:100%;height:467px;background:linear-gradient(180deg,#f1d3b6 0,#f5e4d2 45%,#f7ece2 80%,#d9925b 90%,#d9925b 100%)}
.panel-white{position:absolute;background:var(--white);border:1px solid #e6ddd5}
</style>
</head>
<body>
<div class="board">

<!-- Home -->
<section class="screen" style="left:26px;top:11px;width:368px;height:652px">
  <div class="header" style="height:40px">
    <div class="brand color" style="top:2px">lodgia</div>
    <div class="menu" style="top:14px"></div>
  </div>
  <div class="photo hero" role="img" aria-label="Hourglass on a wooden table in warm light"></div>
  <div class="home-body">
    <div class="home-card">
      <div class="title-hotel">Hotel</div>
      <div class="title-sub">Booking Now</div>
      <div class="search">
        <div class="s-main">Search Hotel</div>
        <div class="s-region">Region ▾</div>
        <div class="s-go"><svg width="16" height="16" viewBox="0 0 16 16"><circle cx="6.5" cy="6.5" r="5" fill="none" stroke="#222" stroke-width="2"/><line x1="10.2" y1="10.2" x2="15" y2="15" stroke="#222" stroke-width="2"/></svg></div>
      </div>
    </div>
  </div>
  <div class="tiles">
    <div class="tile t-leisure"><svg width="24" height="18" viewBox="0 0 24 18"><path d="M2 6 L12 14 L22 6" fill="none" stroke="#fff" stroke-width="2.5"/><circle cx="12" cy="4" r="2.5" fill="#fff"/></svg>LEISURE</div>
    <div class="tile t-food"><svg width="30" height="18" viewBox="0 0 30 18"><path d="M4 14 A11 11 0 0 1 26 14 Z" fill="none" stroke="#fff" stroke-width="2"/><line x1="1" y1="16" x2="29" y2="16" stroke="#fff" stroke-width="2"/><circle cx="15" cy="2.5" r="1.8" fill="#fff"/></svg>FOOD</div>
    <div class="tile t-beauty"><svg width="24" height="20" viewBox="0 0 24 20"><circle cx="12" cy="7" r="5" fill="none" stroke="#fff" stroke-width="1.8"/><path d="M3 19 Q12 10 21 19" fill="none" stroke="#fff" stroke-width="1.8"/></svg>BEAUTY</div>
    <div class="tile t-life"><svg width="24" height="18" viewBox="0 0 24 18"><rect x="3" y="6" width="18" height="10" rx="3" fill="#fff"/><circle cx="9" cy="4" r="3" fill="#fff"/><circle cx="15" cy="4" r="3" fill="#fff"/></svg>LIFE</div>
  </div>
  <div class="badge" style="left:8px;width:84px"></div>
  <div class="badge" style="left:97px;width:82px"></div>
  <div class="login-btn"><svg width="11" height="13" viewBox="0 0 11 13"><rect x="0" y="5" width="11" height="8" rx="1" fill="#111"/><path d="M2.5 5 V3.5 A3 3 0 0 1 8.5 3.5 V5" fill="none" stroke="#111" stroke-width="1.8"/></svg>LOGIN</div>
</section>

<!-- Registration -->
<section class="screen" style="left:418px;top:11px;width:368px;height:652px">
  <div class="header" style="height:64px">
    <div class="back" style="top:28px"></div>
    <div class="brand" style="top:12px">lodgia</div>
    <div class="menu" style="top:28px"></div>
  </div>
  <div class="band" style="top:64px;height:32px"></div>
  <div class="formbar" style="top:96px">REGISTRATION FORM</div>
  <div class="photo" style="top:128px;height:422px;background:linear-gradient(180deg,#e9d3c1 0,#dcc0a8 55%,#b4865e 80%,#8e6240 100%)" role="img" aria-label="Sofa in a bright living room with a pendant lamp"></div>
  <div class="glass" style="left:14px;top:186px;width:340px;height:306px"></div>
  <div class="field" style="left:44px;top:213px;width:274px"><span class="ico"><svg width="12" height="13" viewBox="0 0 12 13"><circle cx="6" cy="4" r="3" fill="none" stroke="#b27fd8" stroke-width="1.2"/><path d="M1 12.5 A5 5 0 0 1 11 12.5 Z" fill="none" stroke="#b27fd8" stroke-width="1.2"/></svg></span>Full Name</div>
  <div class="field teal" style="left:44px;top:252px;width:274px"><span class="ico"><svg width="16" height="11" viewBox="0 0 16 11"><rect x=".6" y=".6" width="14.8" height="9.8" fill="none" stroke="#0f9a94" stroke-width="1.2"/><line x1="8" y1="4" x2="13" y2="4" stroke="#0f9a94"/><line x1="8" y1="7" x2="13" y2="7" stroke="#0f9a94"/></svg></span>ID Number</div>
  <div class="field mag" style="left:44px;top:290px;width:274px"><span class="ico">DOB</span>06/09/1980<svg style="position:absolute;right:8px" width="14" height="14" viewBox="0 0 14 14"><rect x="1" y="2" width="12" height="11" fill="none" stroke="#a0177f" stroke-width="1.6"/><line x1="1" y1="5" x2="13" y2="5" stroke="#a0177f" stroke-width="1.6"/></svg></div>
  <div class="field" style="left:44px;top:328px;width:274px;border-bottom-color:#f0b27a"><span class="ico"><svg width="9" height="14" viewBox="0 0 9 14"><rect x=".5" y=".5" width="8" height="13" rx="1.5" fill="#f0b27a"/></svg></span>Mobile Number</div>
  <div class="field teal" style="left:44px;top:367px;width:274px"><span class="ico"><svg width="14" height="14" viewBox="0 0 14 14"><circle cx="10" cy="4" r="3" fill="#0f9a94"/><line x1="8" y1="6" x2="1" y2="13" stroke="#0f9a94" stroke-width="2"/></svg></span>Set Password</div>
  <div class="field" style="left:44px;top:405px;width:274px"><span class="ico"><svg width="13" height="9" viewBox="0 0 13 9"><rect width="13" height="9" fill="#b27fd8"/><path d="M0 0 L6.5 5 L13 0" fill="none" stroke="#fff"/></svg></span>Email</div>
  <div class="btn" style="left:44px;top:447px;width:274px;height:26px">REGISTER NOW</div>
  <div class="dots" style="top:601px"><i class="d1"></i><i class="d2"></i><i class="d3"></i><i class="d4"></i><i class="d3"></i></div>
</section>

<!-- Login -->
<section class="screen" style="left:802px;top:11px;width:368px;height:652px">
  <div class="header" style="height:74px">
    <div class="back" style="top:26px"></div>
    <div class="brand" style="top:12px">lodgia</div>
    <div class="menu" style="top:26px"></div>
  </div>
  <div class="photo" style="top:74px;height:483px;background:linear-gradient(180deg,#e6b48b 0,#efc8a6 35%,#e8c2a3 60%,#b66f3e 80%,#8a4a22 100%)" role="img" aria-label="Loveseat on a wooden floor in a warm room"></div>
  <div class="glass" style="left:25px;top:204px;width:318px;height:173px"></div>
  <div class="field" style="left:44px;top:225px;width:279px;height:31px"><span class="ico"><svg width="12" height="13" viewBox="0 0 12 13"><circle cx="6" cy="4" r="3" fill="none" stroke="#b27fd8" stroke-width="1.2"/><path d="M1 12.5 A5 5 0 0 1 11 12.5 Z" fill="none" stroke="#b27fd8" stroke-width="1.2"/></svg></span>User Name</div>
  <div class="field teal" style="left:44px;top:265px;width:279px;height:31px"><span class="ico"><svg width="11" height="13" viewBox="0 0 11 13"><rect x=".6" y="5" width="9.8" height="7.4" fill="none" stroke="#0f9a94" stroke-width="1.1"/><path d="M2.5 5 V3.5 A3 3 0 0 1 8.5 3.5 V5" fill="none" stroke="#0f9a94" stroke-width="1.1"/></svg></span>Password</div>
  <div class="abs" style="left:44px;top:304px;font-size:11px;font-weight:500">Register now</div>
  <div class="abs" style="right:47px;top:304px;font-size:11px;color:var(--magenta)">Forgot Password?</div>
  <div class="btn" style="left:45px;top:326px;width:277px;height:27px">LOGIN</div>
  <div class="dots" style="top:601px"><i class="d1"></i><i class="dk"></i><i class="d3"></i><i class="d4"></i><i class="d2"></i></div>
</section>

<!-- Reminder -->
<section class="screen" style="left:26px;top:680px;width:368px;height:512px">
  <div class="header" style="height:62px">
    <div class="back" style="top:22px;left:18px"></div>
    <div class="brand color" style="top:6px">lodgia</div>
    <div class="menu" style="top:20px"></div>
  </div>
  <div class="photo" style="top:62px;height:390px;background:radial-gradient(circle at 80% 65%,#f6ede2 0,#d6b691 40%,#a87a48 100%)" role="img" aria-label="Hanging bulb lamp against a warm wall"></div>
  <div class="remind-card">
    <svg class="abs" style="left:134px;top:26px" width="76" height="76" viewBox="0 0 76 76">
      <circle cx="38" cy="42" r="28" fill="none" stroke="#a0177f" stroke-width="3.5"/>
      <path d="M6 18 A12 12 0 0 1 22 6" fill="none" stroke="#a0177f" stroke-width="3.5"/>
      <path d="M54 6 A12 12 0 0 1 70 18" fill="none" stroke="#a0177f" stroke-width="3.5"/>
      <polyline points="38,26 38,42 50,42" fill="none" stroke="#a0177f" stroke-width="3"/>
      <line x1="18" y1="66" x2="13" y2="73" stroke="#a0177f" stroke-width="3.5"/>
      <line x1="58" y1="66" x2="63" y2="73" stroke="#a0177f" stroke-width="3.5"/>
    </svg>
    <div class="abs" style="left:0;width:100%;top:118px;font-size:17px">Hello Alex Ray,</div>
    <div class="abs" style="left:6px;width:332px;top:151px;font-size:13px;line-height:18px">Your booked time remian 30 mins more. If you want to continue please click continue.</div>
    <div class="choice" style="left:107px;top:200px;width:64px;background:#e0dcd8">1 hour</div>
    <div class="choice" style="left:198px;top:200px;width:64px;background:#e0dcd8">2 hour</div>
    <div class="choice" style="left:114px;top:230px;width:78px;background:var(--teal);color:#fff">Cancel</div>
    <div class="choice" style="left:204px;top:230px;width:78px;background:var(--magenta);color:#fff">Continue</div>
    <div class="abs" style="left:0;width:100%;top:257px;font-size:10px;color:var(--magenta)">* If you continue, charges will be applied hourly.</div>
  </div>
  <div class="abs" style="left:0;top:452px;width:100%;height:60px;background:#f6ede6"></div>
  <div class="dots" style="top:488px"><i class="d1"></i><i class="d2"></i><i class="d3"></i><i class="d4"></i><i class="d2"></i></div>
</section>

<!-- Rating -->
<section class="screen" style="left:418px;top:680px;width:368px;height:512px">
  <div class="header" style="height:45px">
    <div class="back" style="top:18px;left:16px"></div>
    <div class="brand" style="top:2px">lodgia</div>
    <div class="menu" style="top:17px"></div>
  </div>
  <div class="rate-bg" role="img" aria-label="Soft bed linen in warm tones"></div>
  <svg class="abs" style="left:19px;top:58px" width="36" height="36" viewBox="0 0 36 36"><circle cx="18" cy="18" r="17" fill="#fff" stroke="#ccc"/><circle cx="18" cy="14" r="5" fill="none" stroke="#333" stroke-width="1.5"/><path d="M9 27 A9 8 0 0 1 27 27 Z" fill="none" stroke="#333" stroke-width="1.5"/></svg>
  <div class="abs" style="left:61px;top:66px;font-size:15px">Miles Tan</div>
  <div class="abs" style="left:19px;top:103px;width:330px;border-top:1px solid #d8c7b6"></div>
  <div class="abs" style="left:17px;top:110px;width:333px;height:122px;background:linear-gradient(90deg,#b2612e 0,#d9a46a 25%,#39425a 55%,#2b3248 100%)" role="img" aria-label="Hotel room with a bed and a city view at night"></div>
  <div class="abs" style="left:17px;top:202px;width:333px;height:30px;background:rgba(20,20,20,.8);color:#fff;font-size:14px;padding:7px 11px">Hotel Corvina Harbour</div>
  <div class="abs" style="left:17px;top:250px;width:5px;height:29px;background:var(--lilac)"></div>
  <div class="abs" style="left:30px;top:255px;font-size:14px">PLEASE RATE OVERALL SERVICES</div>
  <div class="panel-white" style="left:28px;top:286px;width:319px;height:57px"></div>
  <svg class="abs" style="left:38px;top:299px" width="180" height="30" viewBox="0 0 180 30">
    <defs><polygon id="star" points="15,1 19,11 30,11 21,18 24,29 15,22 6,29 9,18 0,11 11,11"/></defs>
    <use href="#star" fill="#a0177f"/><use href="#star" x="35" fill="#a0177f"/><use href="#star" x="70" fill="#a0177f"/><use href="#star" x="105" fill="#a0177f"/><use href="#star" x="140" fill="#a3a3a3"/>
  </svg>
  <div class="abs" style="left:254px;top:289px;font-size:40px;font-weight:500;color:var(--magenta)">4.0</div>
  <div class="panel-white" style="left:28px;top:354px;width:319px;height:94px;font-size:10px;color:#555;padding:6px 10px">Tell others what you think about us. Would you recommend it, and why?</div>
  <div class="btn" style="left:29px;top:457px;width:318px;height:34px;font-size:15px">SUBMIT</div>
</section>

<!-- Home screen, flat, reduced -->
<section class="screen" style="left:802px;top:680px;width:368px;height:512px;background:#9a9a9a">
  <div class="screen" style="left:55px;top:28px;width:368px;height:652px;transform:scale(0.7);transform-origin:0 0">
    <div class="header" style="height:40px">
      <div class="brand color" style="top:2px">lodgia</div>
      <div class="menu" style="top:14px"></div>
    </div>
    <div class="photo hero" role="img" aria-label="Hourglass on a wooden table in warm light"></div>
    <div class="home-body">
      <div class="home-card">
        <div class="title-hotel">Hotel</div>
        <div class="title-sub">Booking Now</div>
        <div class="search">
          <div class="s-main">Search Hotel</div>
          <div class="s-region">Region ▾</div>
          <div class="s-go"><svg width="16" height="16" viewBox="0 0 16 16"><circle cx="6.5" cy="6.5" r="5" fill="none" stroke="#222" stroke-width="2"/><line x1="10.2" y1="10.2" x2="15" y2="15" stroke="#222" stroke-width="2"/></svg></div>
        </div>
      </div>
    </div>
    <div class="tiles">
      <div class="tile t-leisure">LEISURE</div>
      <div class="tile t-food">FOOD</div>
      <div class="tile t-beauty">BEAUTY</div>
      <div class="tile t-life">LIFE</div>
    </div>
    <div class="badge" style="left:8px;width:84px"></div>
    <div class="badge" style="left:97px;width:82px"></div>
    <div class="login-btn">LOGIN</div>
  </div>
</section>

</div>
</body>
</html>
```